Australian Legal Practice would like a Web Design

I need a web design for a newly established law practice operating as Brindell Legal.

I would like the business to have an internet presence (via a website) essentially for the purpose of marketing and advertising. As the business grows (hopefully) I may be interested in providing general legal information as a means of establishing goodwill in the community and a easy and user friends contact method through the website.

The essence of the business is personal legal service based on local knowledge and therefore i want the website to present a picture of friendly professionalism, but mostly i want people who to be able to find the contact details of the business

I would like to have a map of the office location, and photos of the front of the office, the staff (me at the moment) and picture of law themed items and featuring the Brindell Legal logo.

The areas of law which Brindell Legal practises in are as follows:

commercial law
business sale and purchases
leases
conveyancing and property law
wills and estates
powers of attorney
general legal advice
succession planning
Updates

Target Market(s)

Potential and existing clients of the firm
Other law firms
Associated stakeholders, i.e. Banks and real estate agents

Industry/Entity Type

Law Firm

Coding

Coded - Design and coding required

Number of Pages Required

2 page

Font styles to use
Sans Serif

Colors
85acd3
33a6d7
0456a4

Requirements
Must have
• Brindell Legal logo
• Map of the office location
• Picture of Ross Kedwick (principal solicitor)
• Picture of the office
• Areas of Practice
• Address of office
• email address: ross.kedwick@brindelllegal-example.com.au
• Physical address: 17 Pellow Road, Hamilton VIC 3300
• Phone number: (03) 5598 4731
• Facsimile number: (03) 5598 4706
• Space for a brief description of the firm and its competitive advantage
• Bar Guild Logo
• Links to the Bar Guild of Victoria
• Link to the practitioner oversight Council
Nice to have
• coded to wordpress format

```html
<!DOCTYPE html>
<html lang="en">
<head>
<meta charset="utf-8">
<title>Brindell Legal</title>
<link href="https://fonts.googleapis.com/css2?family=Cinzel:wght@400;700&family=Open+Sans:wght@400;600;700&display=swap" rel="stylesheet">
<style>
:root{
  --navy:#0d3f82;
  --brand:#0456a4;
  --sky:#33a6d7;
  --soft:#85acd3;
  --ink:#4a4f57;
  --dark:#1d2733;
  --dark-2:#2a3646;
  --footer:#2c5a95;
  --footer-deep:#173a6b;
  --paper:#ffffff;
  --line:#d4dce6;
}
*{box-sizing:border-box;margin:0;padding:0}
html,body{width:826px;height:1200px;overflow:hidden;background:var(--paper)}
body{font-family:"Open Sans",Arial,sans-serif;color:var(--ink)}
.page{position:relative;width:826px;height:1200px;overflow:hidden}

/* header */
.site-header{height:62px;display:flex;justify-content:space-between;align-items:flex-start;padding:12px 40px 0}
.brand{display:flex;align-items:center;gap:8px;margin-top:6px;font-weight:700;font-size:22px;color:var(--brand);letter-spacing:1px}
.brand-mark{width:12px;height:12px;background:var(--brand)}
.header-right{display:flex;flex-direction:column;align-items:flex-end;gap:6px}
.phone{display:flex;align-items:center;gap:6px;font-size:12px;font-weight:600;color:var(--navy)}
.main-nav{display:flex;gap:4px}
.main-nav a{font-size:9.5px;font-weight:600;color:var(--navy);text-decoration:none;padding:4px 8px;letter-spacing:.5px}
.main-nav a.current{border:1px solid var(--navy)}

/* hero */
.hero{position:relative;height:308px;background:linear-gradient(135deg,#c9cfd4 0%,#8e979f 35%,#4c5560 70%,#2b323a 100%)}
.hero-title{position:absolute;left:0;right:0;bottom:18px;text-align:center;font-family:"Cinzel",Georgia,serif;font-size:27px;color:#fff;letter-spacing:1.5px;text-shadow:0 1px 3px rgba(0,0,0,.5)}
.hero-band{position:absolute;left:0;right:0;bottom:0;height:60px;background:linear-gradient(to bottom,rgba(20,28,38,0),rgba(20,28,38,.8))}

/* about */
.about{height:260px;padding:26px 40px 0}
.section-heading{display:flex;align-items:flex-end;gap:10px;border-bottom:1px solid var(--line);padding-bottom:6px;width:360px}
.section-heading h2{font-family:"Cinzel",Georgia,serif;font-weight:400;font-size:22px;color:var(--brand);letter-spacing:1px}
.about-body{display:flex;gap:22px;margin-top:22px}
.portrait{width:130px;height:150px;flex:none;background:linear-gradient(180deg,#dfe7ef 0%,#9fb3c8 60%,#3c5777 100%)}
.about-body p{font-size:9px;line-height:1.75;color:var(--ink);text-align:justify}

/* practice + why */
.feature{position:relative;height:320px;background:linear-gradient(120deg,var(--dark) 0%,var(--dark-2) 55%,#3a4858 100%);color:#fff;display:flex;padding:28px 40px 0;gap:40px}
.feature-col{flex:1}
.split-heading{font-family:"Cinzel",Georgia,serif;font-size:17px;letter-spacing:1.5px;line-height:1.4;border-bottom:1px solid rgba(255,255,255,.4);padding-bottom:4px;margin-bottom:14px}
.split-heading span{display:block}
.split-heading span+span{padding-left:80px}
.practice-list{list-style:none}
.practice-list li{display:flex;align-items:center;gap:12px;font-size:11px;height:28px}
.why-text{font-size:9px;line-height:1.7;color:#d9e2ec;margin-bottom:12px}
.tick-list{list-style:none}
.tick-list li{display:flex;align-items:center;gap:12px;font-size:10px;height:27px}

/* footer */
.site-footer{height:210px;background:var(--footer);color:#fff;display:flex;padding:20px 40px 0;gap:26px}
.footer-col h3{font-size:10px;font-weight:700;letter-spacing:1px;margin-bottom:12px}
.contact-col{width:160px}
.contact-line{display:flex;gap:7px;font-size:8.5px;line-height:1.4;margin-bottom:9px;align-items:flex-start}
.map-col{width:150px}
.map{width:150px;height:100px;background:linear-gradient(135deg,#e4eaf0,#c5d3df)}
.news-col{width:170px}
.news-col p{font-size:8.5px;line-height:1.5;margin-bottom:10px;color:#e1e9f3}
.news-input{height:22px;background:#fff;color:#8a939d;font-size:8.5px;padding:5px 7px;margin-bottom:8px}
.news-btn{display:inline-block;background:var(--footer-deep);font-size:9px;font-weight:700;padding:5px 12px;letter-spacing:1px}
.badges{margin-left:auto;display:flex;flex-direction:column;gap:12px}
.badge{width:96px;height:60px;background:#fff}
.badge.second{background:#5a4a8a}

.bottom-bar{height:40px;background:var(--footer-deep);color:#cfdbea;display:flex;justify-content:space-between;align-items:center;padding:0 40px;font-size:8px}
.bottom-links{display:flex;flex-direction:column;gap:3px}
.social{display:flex;gap:6px}
.social span{width:16px;height:16px;border-radius:50%;background:#fff}
</style>
</head>
<body>
<div class="page">

  <header class="site-header">
    <div class="brand"><span class="brand-mark"></span>Brindell Legal</div>
    <div class="header-right">
      <div class="phone">
        <svg width="12" height="12" viewBox="0 0 24 24"><circle cx="12" cy="12" r="12" fill="#0456a4"/><path d="M8 6l2 0 1 3-1.5 1a8 8 0 0 0 4.5 4.5l1-1.5 3 1 0 2c0 1-1 2-2 2A11 11 0 0 1 6 8c0-1 1-2 2-2z" fill="#fff"/></svg>
        (03) 5598 4731
      </div>
      <nav class="main-nav">
        <a class="current" href="#">HOME</a>
        <a href="#">ABOUT US</a>
        <a href="#">AREAS OF PRACTICE</a>
        <a href="#">CONTACT US</a>
      </nav>
    </div>
  </header>

  <section class="hero" role="img" aria-label="Photo of the legal team meeting around a desk in the office">
    <div class="hero-band"></div>
    <h1 class="hero-title">We Are The Best Law Firm In Hamilton</h1>
  </section>

  <section class="about">
    <div class="section-heading"><h2>About Brindell Legal</h2></div>
    <div class="about-body">
      <div class="portrait" role="img" aria-label="Portrait of principal solicitor Ross Kedwick"></div>
      <p>Brindell Legal is a newly established practice in Hamilton offering personal legal service built on local knowledge. We work closely with individuals, families and businesses across the district, giving clear advice in plain language and practical help at every step. Whether you are buying a property, selling a business, planning your estate or signing a lease, we take time to understand your situation and explain your options. Our principal solicitor brings years of experience in commercial and property matters, and every client deals directly with him from first meeting to final settlement. We keep our fees transparent, return calls promptly and are always happy to meet at a time that suits you. Call in to our office on Pellow Road or contact us by phone or email to arrange a consultation.</p>
    </div>
  </section>

  <section class="feature" aria-label="Areas of practice and why choose us">
    <div class="feature-col">
      <h2 class="split-heading"><span>Areas of Law</span><span>Practices</span></h2>
      <ul class="practice-list">
        <li><svg width="14" height="14" viewBox="0 0 14 14"><rect x="2" y="1" width="10" height="12" fill="none" stroke="#fff" stroke-width="1.3"/><path d="M4 5h6M4 8h6" stroke="#fff"/></svg>Commercial Law</li>
        <li><svg width="14" height="14" viewBox="0 0 14 14"><rect x="1" y="4" width="12" height="8" fill="none" stroke="#fff" stroke-width="1.3"/><rect x="5" y="2" width="4" height="2" fill="none" stroke="#fff"/></svg>Business Sale And Purchases</li>
        <li><svg width="14" height="14" viewBox="0 0 14 14"><path d="M2 13V6l5-4 5 4v7z" fill="none" stroke="#fff" stroke-width="1.3"/></svg>Leases</li>
        <li><svg width="14" height="14" viewBox="0 0 14 14"><path d="M1 13V6l6-5 6 5v7H9V9H5v4z" fill="#fff"/></svg>Conveyancing And Property Law</li>
        <li><svg width="14" height="14" viewBox="0 0 14 14"><path d="M3 1h6l3 3v9H3z" fill="none" stroke="#fff" stroke-width="1.3"/></svg>Wills And Estates</li>
        <li><svg width="14" height="14" viewBox="0 0 14 14"><path d="M7 1v12M2 4h10M2 4l-1 4h3zM12 4l-1 4h3z" fill="none" stroke="#fff" stroke-width="1.2"/></svg>Powers of Attorney</li>
        <li><svg width="14" height="14" viewBox="0 0 14 14"><circle cx="7" cy="7" r="5.5" fill="none" stroke="#fff" stroke-width="1.3"/><path d="M7 6v4M7 4v.5" stroke="#fff" stroke-width="1.4"/></svg>General Legal Advice</li>
        <li><svg width="14" height="14" viewBox="0 0 14 14"><circle cx="7" cy="4" r="2.5" fill="#fff"/><path d="M2 13c0-3 2-5 5-5s5 2 5 5z" fill="#fff"/></svg>Succession Planning</li>
      </ul>
    </div>
    <div class="feature-col">
      <h2 class="split-heading"><span>Why</span><span>Choose Us</span></h2>
      <p class="why-text">Local people deserve a local lawyer. We know Hamilton, its businesses and its property market, and we bring that knowledge to every matter we handle.</p>
      <ul class="tick-list">
        <li><svg width="16" height="16" viewBox="0 0 16 16"><path d="M2 8l4 4 8-9" fill="none" stroke="#fff" stroke-width="2.2"/></svg>Personal service from your own solicitor</li>
        <li><svg width="16" height="16" viewBox="0 0 16 16"><path d="M2 8l4 4 8-9" fill="none" stroke="#fff" stroke-width="2.2"/></svg>Clear advice in plain everyday language</li>
        <li><svg width="16" height="16" viewBox="0 0 16 16"><path d="M2 8l4 4 8-9" fill="none" stroke="#fff" stroke-width="2.2"/></svg>Transparent fees agreed before we start</li>
        <li><svg width="16" height="16" viewBox="0 0 16 16"><path d="M2 8l4 4 8-9" fill="none" stroke="#fff" stroke-width="2.2"/></svg>Local knowledge of Hamilton and district</li>
        <li><svg width="16" height="16" viewBox="0 0 16 16"><path d="M2 8l4 4 8-9" fill="none" stroke="#fff" stroke-width="2.2"/></svg>Prompt replies to calls and emails</li>
        <li><svg width="16" height="16" viewBox="0 0 16 16"><path d="M2 8l4 4 8-9" fill="none" stroke="#fff" stroke-width="2.2"/></svg>Convenient appointments at our office</li>
      </ul>
    </div>
  </section>

  <footer class="site-footer">
    <div class="footer-col contact-col">
      <h3>CONTACT INFORMATION</h3>
      <div class="contact-line"><svg width="10" height="12" viewBox="0 0 10 12"><path d="M5 0a4 4 0 0 1 4 4c0 3-4 8-4 8S1 7 1 4a4 4 0 0 1 4-4z" fill="#fff"/><circle cx="5" cy="4" r="1.5" fill="#2c5a95"/></svg>17 Pellow Road,<br>Hamilton VIC 3300</div>
      <div class="contact-line"><svg width="10" height="10" viewBox="0 0 24 24"><path d="M6 2l4 0 2 5-3 2a12 12 0 0 0 6 6l2-3 5 2 0 4c0 2-2 4-4 4A18 18 0 0 1 2 6c0-2 2-4 4-4z" fill="#fff"/></svg>(03) 5598 4731</div>
      <div class="contact-line"><svg width="10" height="10" viewBox="0 0 10 10"><rect x="1" y="3" width="8" height="6" fill="#fff"/><rect x="3" y="0.5" width="4" height="3" fill="none" stroke="#fff"/></svg>(03) 5598 4706</div>
      <div class="contact-line"><svg width="10" height="10" viewBox="0 0 10 10"><rect x="0.5" y="2" width="9" height="6.5" fill="#fff"/><path d="M0.5 2l4.5 4 4.5-4" fill="none" stroke="#2c5a95"/></svg>ross.kedwick@brindelllegal-example.com.au</div>
    </div>
    <div class="footer-col map-col">
      <h3>LOCATION MAP</h3>
      <div class="map" role="img" aria-label="Street map showing the office on Pellow Road, Hamilton"></div>
    </div>
    <div class="footer-col news-col">
      <h3>NEWSLETTER SIGNUP</h3>
      <p>Sign up for practical legal updates and news from our office.</p>
      <div class="news-input">Your email address</div>
      <span class="news-btn">SUBMIT</span>
    </div>
    <div class="badges">
      <a class="badge" href="#" aria-label="Bar Guild of Victoria"></a>
      <a class="badge second" href="#" aria-label="practitioner oversight Council"></a>
    </div>
  </footer>

  <div class="bottom-bar">
    <div class="bottom-links">
      <span>Home | About Us | Areas of Practice | Why Choose Us | Support | Contact Us</span>
      <span>Copyright 2015 Brindell Legal. All rights reserved.</span>
    </div>
    <div class="social" aria-label="Social links"><span></span><span></span><span></span><span></span></div>
  </div>

</div>
</body>
</html>
```